Creative Realtor Business Card Design

I need a creative business card.... I would like it to be larger than the normal size...heavy stock.... colorful...
As you are probably aware, there are tons of realtors, and most of their cards ALL look alike.. potential clients are looking for agents that are professional, but are different.
Cards are a form of advertising and I need your help to make mine stand out in a professional, classy way.
I don't need to use the harbor sage realty logo, my personal logo is MORE important for branding purposes. OR..what is your opinion?
YOU DESIGN FOR ME PLEASE! If I could do what you do I would.... I can't and I need your professional help.

                                        If you think I need the card to be double sided so it doesn't look busy by all means I will happily accept double sided. 

I am very interested in a more "creative" card than a standard run of the mill realtor card.    I care about my clients LONG after the sale has closed!

                                   

THANK YOU SO MUCH FOR YOUR EFFORTS AND TALENTS....I APPRECIATE IT SO MUCH! 

                                        Would it be possible to use my theme of my logo to design my card?

                                            Where Keys Meet Kindred Spirits

                              

 

Please make cards larger size .... See this link for ideas that appeal to me. Thank you for your interest.

https://www.lookwidely.example/find?q=examples+of+unique+business+cards&mode=img&ref=7QpL2xV9

I want my card to stand out in size and design...

Thank you so much for your hard work for me.

Lorna

 

Reason: I learned that many designers are very busy. I am providing more time and money in hopes that designers will find it an attractive enough challenge to participate. My business cards are one of my most important marketing materials...I NEED THEM TO BE DISTINCTIVE, CLASSY, and INFORMATIVE. Thank you SO MUCH....and I will be anxiously awaiting your great designs... Lorna

Hello Designers,

Thank you to all you creative people that have kindly offered to submit your creative design(s) for my business card.  I view your designs as your creative artwork. I am anxious to see where your creativity leads you.

I wanted to share with you that my logo was something I personally designed after being in business for 3  years. ( I did have to have a professionals like yourselves draw it for me). The design and logo captured perfectly how I felt about my work ...helping individuals, such as you, find a home.  A house is easy to find, but a home is a place that has "good" energy ... a place where you feel comfortable and can grow.  A place that just "Feels right!"  It's one of those things that you just KNOW when it is right! 

I hope by sharing this bit of information about me can help you creatively design my card for me...I care for my clients LONG after the transaction has closed and they are in their home. Thank you again for taking the time to work on my design. I have been adding money so that your time spent on my card is worth it.

I do need my card soon...so please, if you have a design...submit it!

Kind Regards,

Lorna

Target Market(s)

I have a variety of clients from a mobile home of $35,000 to an estate property for $5M. I feel comfortable working with all types of people...I love my job...I love helping people find the right home because we all know how our home environment affects our well being.

Industry/Entity Type

Advertising

Contact Information for Business Card

Lorna Pratley, Realtor
Harbor Sage Realty
"Where Keys Meet Kindred Spirits"
www.lornanestfinder.example
lpratley@mailbarn.example
(555) 418-2093
BRE #04872351, Exp. 8/15

Colors

Designer to choose colors to be used in the design.

Requirements
Must have
• By law, my license number information MUST be on my card.
Nice to have
• I would love card to be memorable...if that is possible for a business card. Also, I would like my card to be larger than the average card. Not sure that is possible either.

```html
<!DOCTYPE html>
<html lang="en">
<head>
<meta charset="utf-8">
<title>Lorna Pratley – Key Business Card</title>
<link rel="stylesheet" href="https://fonts.googleapis.com/css2?family=Roboto+Condensed:wght@400;500&family=Tinos:wght@400&family=Share+Tech+Mono&display=swap">
<style>
  :root {
    --backdrop-light: #f1f1f2;
    --backdrop-dark: #c9cacc;
    --key-black: #000000;
    --key-outline: #ffffff;
    --stripe-green: #1f7f52;
    --heart-red: #e0393e;
    --ink-white: #ffffff;
    --hole: #e4e5e6;
  }
  html, body {
    margin: 0;
    width: 1200px;
    height: 900px;
    overflow: hidden;
  }
  body {
    background: radial-gradient(ellipse at 50% 30%, var(--backdrop-light) 0%, #e2e3e4 55%, var(--backdrop-dark) 100%);
  }
  .key-card { display: block; width: 1200px; height: 900px; }
  .key-body { fill: var(--key-black); stroke: var(--key-outline); stroke-width: 1.5; }
  .stripe { fill: var(--stripe-green); }
  .key-hole { fill: var(--hole); stroke: var(--key-outline); stroke-width: 1.5; }
  .brokerage { font-family: "Roboto Condensed", sans-serif; font-size: 22px; fill: var(--ink-white); }
  .tagline { font-family: "Share Tech Mono", monospace; font-style: italic; font-size: 16px; fill: var(--ink-white); }
  .tagline-mid { fill: var(--heart-red); }
  .agent-name { font-family: "Tinos", serif; fill: var(--ink-white); }
  .agent-role { font-family: "Roboto Condensed", sans-serif; font-size: 18px; fill: var(--ink-white); }
  .brand-dot { fill: var(--heart-red); }
  .license, .contact { font-family: "Share Tech Mono", monospace; fill: var(--ink-white); }
  .license { font-size: 21px; }
  .contact { font-size: 18px; }
</style>
</head>
<body>
<svg class="key-card" viewBox="0 0 1200 900" xmlns="http://www.w3.org/2000/svg">
  <defs>
    <clipPath id="front-key-clip">
      <path d="M310 400 L42 400 L12 432 L42 462 L72 462 L96 480 L120 462 L142 490 L166 468 L188 480 L212 478 L238 500 L262 500 L262 524 L310 524 A158 158 0 1 0 310 400 Z"/>
    </clipPath>
    <clipPath id="back-key-clip">
      <path d="M890 400 L1158 400 L1188 432 L1158 462 L1128 462 L1104 480 L1080 462 L1058 490 L1034 468 L1012 480 L988 478 L962 500 L938 500 L938 524 L890 524 A158 158 0 1 1 890 400 Z"/>
    </clipPath>
  </defs>

  <g class="key front-key">
    <path class="key-body" d="M310 400 L42 400 L12 432 L42 462 L72 462 L96 480 L120 462 L142 490 L166 468 L188 480 L212 478 L238 500 L262 500 L262 524 L310 524 A158 158 0 1 0 310 400 Z"/>
    <g class="key-stripes" clip-path="url(#front-key-clip)">
      <rect class="stripe" x="0" y="429" width="600" height="4"/>
      <rect class="stripe" x="0" y="438" width="600" height="4"/>
      <rect class="stripe" x="0" y="447" width="600" height="4"/>
      <rect class="stripe" x="0" y="456" width="600" height="4"/>
      <rect class="stripe" x="0" y="465" width="600" height="4"/>
      <rect class="stripe" x="0" y="474" width="600" height="4"/>
      <rect class="stripe" x="0" y="483" width="600" height="4"/>
      <rect class="stripe" x="0" y="492" width="600" height="4"/>
    </g>
    <circle class="key-hole" cx="512" cy="465" r="38"/>

    <text class="brokerage" x="72" y="423">Harbor Sage Realty</text>

    <text class="tagline" text-anchor="middle">
      <tspan x="483" y="345">Where Keys</tspan>
      <tspan class="tagline-mid" x="483" y="363">Meet</tspan>
      <tspan x="481" y="384">Kindred Spirits</tspan>
    </text>

    <circle class="brand-dot" cx="396" cy="460" r="26"/>
    <text class="agent-name" x="400" y="538" font-size="26" text-anchor="middle" textLength="146" lengthAdjust="spacingAndGlyphs">LORNA PRATLEY</text>
  </g>

  <g class="key back-key">
    <path class="key-body" d="M890 400 L1158 400 L1188 432 L1158 462 L1128 462 L1104 480 L1080 462 L1058 490 L1034 468 L1012 480 L988 478 L962 500 L938 500 L938 524 L890 524 A158 158 0 1 1 890 400 Z"/>
    <g class="key-stripes" clip-path="url(#back-key-clip)">
      <rect class="stripe" x="600" y="429" width="600" height="4"/>
      <rect class="stripe" x="600" y="438" width="600" height="4"/>
      <rect class="stripe" x="600" y="447" width="600" height="4"/>
      <rect class="stripe" x="600" y="456" width="600" height="4"/>
      <rect class="stripe" x="600" y="465" width="600" height="4"/>
      <rect class="stripe" x="600" y="474" width="600" height="4"/>
      <rect class="stripe" x="600" y="483" width="600" height="4"/>
      <rect class="stripe" x="600" y="492" width="600" height="4"/>
    </g>
    <circle class="key-hole" cx="680" cy="465" r="38"/>

    <text class="license" text-anchor="middle">
      <tspan x="745" y="368">BRE #04872351,</tspan>
      <tspan x="745" y="397">Expiry Date. 8/2015</tspan>
    </text>

    <text class="agent-name" x="1084" y="424" font-size="32" text-anchor="end" textLength="206" lengthAdjust="spacingAndGlyphs">LORNA PRATLEY</text>
    <rect fill="var(--key-black)" x="1006" y="433" width="80" height="24"/>
    <text class="agent-role" x="1084" y="452" text-anchor="end">REALTOR</text>
    <circle class="brand-dot" cx="1130" cy="442" r="26"/>

    <text class="contact" text-anchor="middle">
      <tspan x="735" y="534">(555) 418-2093</tspan>
      <tspan x="745" y="558" textLength="216" lengthAdjust="spacingAndGlyphs">www.lornanestfinder.example</tspan>
      <tspan x="745" y="582" textLength="190" lengthAdjust="spacingAndGlyphs">lpratley@mailbarn.example</tspan>
    </text>
  </g>
</svg>
</body>
</html>
```